Post Card Mailer for QUIK PATH PROSPECTS using new logo

We need a post card designed to send through the USA mail service that will go to new prospective clients.

The post card will introduce me and my new company and try to educate them our on company and services.

The goal is for them to call me or email me so I can have a discussion and try to sell our product.

Our product is a name list of individuals that are looking for consulting / help to determine if they qualify for USA social security benefits and then help to manage the process. We sell this name list to law firms that help these individuals.

Our services are better because we have a better less expensive way to identify people via the internet that want help. Our conversion rate is 15%, so every 100 leads a law firm buys the will obtain 15 customers / clients.

Designer on Logo took alot longer than expected. Also there were two projects that needed to combined into one. Which was done yesterday.

Target Market(s)

Law firms

Font styles to use
Serif
Sans Serif
Script

Colors

Designer to choose colors to be used in the design.

Requirements
Must have
• The size of the mailer should be about 6 by 8 inches.
• Two sides.
• Side 1: With our Logo and key messages we want to communicate.
• Side 2: A space to be used by the USA mail services in lower right, my photo and an introduction by me to our company and why they should buy from my company.
Nice to have
• Images that represent what we do, how we help, and our target market.
Should not have
• Poor taste in images that upset people

```html
<!DOCTYPE html>
<html lang="en">
<head>
<meta charset="utf-8">
<title>Quik Path Prospects Mailer</title>
<link href="https://fonts.googleapis.com/css2?family=Montserrat:wght@300;400;700;800&family=Lato:wght@400;700&display=swap" rel="stylesheet">
<style>
:root{
  --bg:#d2d3d5;
  --blue:#2b7bc0;
  --gray-light:#d1d2d4;
  --col-a:#6e6f71;
  --col-b:#8c8d8f;
  --col-c:#78797b;
  --col-d:#909193;
  --footer:#333335;
  --ink:#58595b;
  --white:#ffffff;
}
*{margin:0;padding:0;box-sizing:border-box}
html,body{width:845px;height:1200px;overflow:hidden;background:var(--bg)}
body{position:relative;font-family:'Lato',sans-serif}
.card{position:absolute;left:124px;width:597px;height:448px;overflow:hidden;box-shadow:0 2px 6px rgba(0,0,0,.18)}
.card--front{top:134px;background:var(--white)}
.card--back{top:654px;background:var(--white)}
.abs{position:absolute}

/* front */
.hero-photo{left:0;top:0;width:597px;height:172px;background:linear-gradient(100deg,#e9dccd 0%,#f2ece4 45%,#f6f3ef 70%,#ece8e4 100%)}
.hero-wedge{left:0;top:0}
.brand{font-family:'Montserrat',sans-serif;font-weight:800;color:var(--blue);line-height:1;letter-spacing:1px}
.brand--front{left:352px;top:44px;font-size:31px}
.headline-band{left:0;top:171px;width:597px;height:128px;background:var(--blue);color:var(--white);padding:27px 0 0 33px;font-family:'Montserrat',sans-serif}
.headline{font-size:24.5px;line-height:25px;font-weight:400;text-transform:uppercase}
.headline b{font-weight:800}
.tagline{margin-top:12px;font-size:19px;font-weight:300;letter-spacing:2.3px}
.features{left:0;top:299px;width:597px;height:116px;display:flex}
.feature{width:149.25px;height:116px;padding:16px 10px 0 24px;color:var(--white)}
.feature:nth-child(1){background:var(--col-a)}
.feature:nth-child(2){background:var(--col-b);padding-left:16px}
.feature:nth-child(3){background:var(--col-c);padding-left:15px}
.feature:nth-child(4){background:var(--col-d);padding-left:24px}
.feature h3{font-size:11.5px;font-weight:700;line-height:13.5px;margin-bottom:10px}
.feature ul{list-style:none;font-size:9px;line-height:11px}
.feature li{position:relative;padding-left:9px;margin-bottom:3px}
.feature li::before{content:"•";position:absolute;left:0}
.site-bar{left:0;top:415px;width:597px;height:33px;background:var(--footer);color:var(--white);font-family:'Montserrat',sans-serif;font-size:14px;letter-spacing:3.2px;text-align:center;line-height:33px}

/* back */
.intro-panel{left:0;top:0;width:310px;height:448px;background:var(--blue)}
.offer-panel{left:0;top:0}
.portrait{left:36px;top:27px;width:124px;height:124px;border-radius:50%;border:2px solid var(--white);background:radial-gradient(circle at 50% 40%,#8a8f96,#3b4048)}
.sender-name{left:173px;top:95px;color:var(--white)}
.sender-name strong{display:block;font-size:16px;font-weight:400}
.sender-name span{font-size:10.5px}
.intro{left:38px;top:164px;width:262px;color:var(--white)}
.intro h2{font-size:16px;font-weight:400;line-height:19px;margin-bottom:6px}
.intro ul{list-style:none;font-size:10px;line-height:12.3px}
.intro li{position:relative;padding-left:24px;margin-bottom:3px}
.intro li::before{content:"•";position:absolute;left:6px}
.pledge{left:42px;top:390px;width:249px;height:37px;border:1px solid var(--white);color:var(--white);font-size:10.5px;line-height:12.5px;text-align:center;padding-top:5px}
.brand--back{left:360px;top:52px;font-size:32px}
.test-banner{left:348px;top:141px}
.offer{left:352px;top:189px;list-style:none;font-size:10px;line-height:16px;color:#333}
.offer li{position:relative;padding-left:22px}
.offer li::before{content:"•";position:absolute;left:2px}
.return-address{left:333px;top:262px;font-size:8px;line-height:10.5px;color:var(--ink)}
.postage{left:521px;top:266px;width:51px;height:54px;border:1px solid #b8b9bb;font-size:10px;color:var(--ink);display:flex;align-items:center;justify-content:center}
.addressee{left:392px;top:371px;font-size:10px;color:#8a8b8d}
</style>
</head>
<body>

<section class="card card--front">
  <div class="abs hero-photo" role="img" aria-label="Photo of a caregiver helping a smiling senior woman walk in a bright home"></div>
  <svg class="abs hero-wedge" width="597" height="172" viewBox="0 0 597 172"><polygon points="508,172 597,98 597,172" fill="#2b7bc0"/></svg>
  <div class="abs brand brand--front">QUIK PATH<br>PROSPECTS</div>
  <div class="abs headline-band">
    <p class="headline"><b>Best leads … best price</b> with<br><b>High volume</b> &amp; quality capacity …</p>
    <p class="tagline">Leads from a Trusted Partner that is easy to use</p>
  </div>
  <div class="abs features">
    <div class="feature">
      <h3>Best Leads,<br>Best Price</h3>
      <ul><li>Our high conversation rates lowers your client acquisition cost</li><li>Referrals available</li></ul>
    </div>
    <div class="feature">
      <h3>High Volume,<br>Quality Leads</h3>
      <ul><li>50 years of SSD domain knowledge</li><li>Tested technology capabilities</li></ul>
    </div>
    <div class="feature">
      <h3>Trusted Partner</h3>
      <ul><li>Reliability, Dependable, Helpful</li><li>Deep business &amp; process acumen</li></ul>
    </div>
    <div class="feature">
      <h3>Easy to use</h3>
      <ul><li>Integrate seamlessly into your IT systems</li><li>Tailored campaigns</li></ul>
    </div>
  </div>
  <div class="abs site-bar">www.QuikPathProspects.com</div>
</section>

<section class="card card--back">
  <svg class="abs offer-panel" width="597" height="448" viewBox="0 0 597 448"><polygon points="310,70 366,0 597,0 597,242 310,242" fill="#d1d2d4"/></svg>
  <div class="abs intro-panel" style="clip-path:polygon(0 0,366px 0,310px 70px,310px 448px,0 448px)"></div>
  <div class="abs portrait" role="img" aria-label="Portrait photo of the company president"></div>
  <div class="abs sender-name"><strong>Dalton Hewitt</strong><span>President, Quik Path Prospects</span></div>
  <div class="abs intro">
    <h2>I want to personally introduce our company to you!</h2>
    <ul>
      <li>My team as &gt; 50 years of cumulative SSD experience.</li>
      <li>We have proven technology that delivers the best leads.</li>
      <li>The timing is right for a new competitor in this industry.</li>
      <li>I had to come out of retirement after 30 years with Norvale Industries, the opportunity is just that great … I love building businesses and partnering with great customers!</li>
      <li>Our business, industry, &amp; technical acumen is unrivaled … and we can do it at a cost than no others can.</li>
    </ul>
  </div>
  <div class="abs pledge">Let’s work together to bring Social Security<br>Disability benefits to those in need and deserving!</div>

  <div class="abs brand brand--back">QUIK PATH<br>PROSPECTS</div>
  <svg class="abs test-banner" width="214" height="38" viewBox="0 0 214 38">
    <polygon points="0,9 180,9 180,0 214,19 180,38 180,29 0,29" fill="#2b7bc0"/>
    <polygon points="0,8 180,8 180,30 0,30" fill="#2b7bc0"/>
    <text x="10" y="27" font-family="Montserrat, sans-serif" font-weight="800" font-size="18" fill="#fff" letter-spacing="1">TEST OUR LEADS</text>
  </svg>
  <ul class="abs offer">
    <li>Start at 250 or 500 Leads.</li>
    <li>Grow to 1,000 … 3,000 or even 10,000!</li>
    <li>We give the right support to your growth.</li>
  </ul>
  <div class="abs return-address">Dalton Hewitt, President Quik Path Prospects<br>2210 Orchard Lane, Suite 400<br>Dayton Ohio OH 45402<br>555-014-2290<br>Dalton@QuikPathProspects.com</div>
  <div class="abs postage">Postage</div>
  <div class="abs addressee">To:&nbsp; Addressee</div>
</section>

</body>
</html>
```